Velmora Outcomes Brochure Design Project

- Who we are?
Velmora Outcomes is New Internet Marketing Company Based in China.

It is our aim to provide Chinese clients with the means to internationally market their product, via the Internet.

Our primary products are Outsourced Design ( Thanks to Pixel hive and the amazing designers who use it), SEO and Virtual Hosting.

- Project Brief
Design a vibrant and fresh brochure that introduces the fundamentals of SEO. There is no restriction to the number of pages, however all the info I have included in this brief must be included.

- Colour Palette
Please see link or download the Adobe Swatch Exchange File or follow the link below
http://tintaro.example.com/#themes/search?term=5830716
Updates

Logo updated - grey background removed

Various file formats added for logo and brochure content

Brochure zip file add containing logo in different formats.

Adobe color scheme file added

The general corporate colors are:

Base Color: CMYK :0, 60, 80, 0  Hex: FF6633
Dark Orange: CMYK: 0, 72, 96, 30 Hex: B23308
Light Orange: CMYK 0, 42, 56, 0 Hex: FF9571
Grey: CMYK 0, 0, 0, 48 Hex: 858585
Light Grey: CMYK 0, 0, 0, 26 Hex: BDBDBD

Please note that I'm happy for other colors to be included, however I would like these the corporate branding colors to be clearly present through the brochure.

Hi All

First place payment has increased to $600 - Looking to see some creative designs!

Hi All

Project Deadline Extended
Reason: I have increase the budget and extend the deadline as I need to see more design.

I have attached a zip file that contains example brochures I like.

We are not keen on the table data its a little plain. We have create an info-graphic to replace one of the table and would like to see it included in the design.

Project Deadline Extended
Reason: A few designers have asked for this extension and I would like to see additional designs. Thanks Marek

Target Market(s)

- Our Target Audience is..
It is small to medium businesses looking to reach out to the international market.
Our clients still very much operate on a face to face level in business and are new to the concept of Internet marketing

However this must look professional, Marketable and Clean, with the power of connecting people globally, through SEO and design to be reflected visually in the brochure.

Industry/Entity Type

Internet

Requirements
Must have
• One or more of the FACTS that I have highlighted need to stand out on each page. These FACTS can be found the document attached to this brief and are under the section titled 'Did You Know!'. Not every fact in this section needs to be highlighted in the brochure, but each page needs to have at least, one or more fact that stands out, soemwhere on the page.
See attached document, under the heading 'Did you Know!' and use one or two of these facts to spruce up the pages!

One image/ per page or per two pages MUST be included!

- Provide stock photos and please send us a message with the additional cost of these with your submission

The Table data, that I have included in the attachment must be included in the body of the pages - BUT the table format is not necessary and you can place the information in the body like plain text.

The brochure size should be a little larger than A4.

Please design the back page, like a pocket to hold paper and other material in it that I include with this brochure.

```html
<!DOCTYPE html>
<html lang="en">
<head>
<meta charset="utf-8">
<title>Velmora Outcomes – SEO Brochure Spread</title>
<link href="https://fonts.googleapis.com/css2?family=Carlito:ital,wght@0,400;0,700;1,700&family=Tinos:wght@700&family=PT+Sans&display=swap" rel="stylesheet">
<style>
  :root {
    --page-red: #b3161c;
    --page-red-deep: #6e0a0e;
    --base-orange: #ff6633;
    --dark-orange: #b23308;
    --light-orange: #ff9571;
    --grey: #858585;
    --light-grey: #bdbdbd;
    --white: #ffffff;
    --ink: #222222;
    --rule: #e7a592;
    --folio: #000000;
  }
  html, body {
    margin: 0;
    padding: 0;
    width: 1200px;
    height: 900px;
    overflow: hidden;
    background: var(--white);
  }
  .canvas {
    position: relative;
    width: 1200px;
    height: 900px;
    background: var(--white);
  }
  .page {
    position: absolute;
    top: 40px;
    height: 805px;
    overflow: hidden;
    background: radial-gradient(ellipse at 45% 40%, var(--page-red-deep) 0%, #8c0f14 35%, var(--page-red) 75%);
  }
  .page--left { left: 18px; width: 580px; }
  .page--right { left: 600px; width: 572px; background: radial-gradient(ellipse at 40% 45%, #8c0f14 0%, var(--page-red) 60%, #c01d22 100%); }

  .section-tab {
    position: absolute;
    top: 28px;
    height: 28px;
    background: linear-gradient(var(--base-orange), #f0521f);
    color: var(--white);
    font-family: "Tinos", "Times New Roman", serif;
    font-weight: 700;
    font-size: 20px;
    line-height: 28px;
    text-align: center;
    text-shadow: 0 1px 1px rgba(0,0,0,.35);
  }
  .page--left .section-tab {
    left: 37px; width: 78px;
    clip-path: polygon(0 0, 88% 0, 100% 50%, 88% 100%, 0 100%);
    padding-right: 6px; box-sizing: border-box;
  }
  .page--right .section-tab {
    left: 460px; width: 112px;
    clip-path: polygon(12% 0, 100% 0, 100% 100%, 12% 100%, 0 50%);
    padding-left: 6px; box-sizing: border-box;
  }

  .fact {
    position: absolute;
    top: 27px;
    height: 36px;
    background: linear-gradient(var(--base-orange), #f04e1c);
    border-radius: 0 0 4px 4px;
    color: var(--white);
    font-family: "Carlito", Calibri, sans-serif;
    font-style: italic;
    font-weight: 700;
    font-size: 9.5px;
    line-height: 11px;
    box-sizing: border-box;
  }
  .fact__label {
    position: absolute;
    top: -2px;
    height: 13px;
    padding: 0 6px;
    background: var(--white);
    border-radius: 6px;
    color: var(--dark-orange);
    font-style: normal;
    font-size: 10px;
    line-height: 13px;
    display: flex;
    align-items: center;
    gap: 4px;
  }
  .fact__label svg { width: 9px; height: 9px; }
  .fact--left { left: 279px; width: 270px; text-align: right; padding: 14px 8px 0 8px; }
  .fact--left .fact__label { right: 2px; }
  .fact--right { left: 20px; width: 190px; padding: 14px 6px 0 6px; }
  .fact--right .fact__label { left: 2px; }

  .intro {
    position: absolute;
    left: 27px;
    top: 80px;
    width: 522px;
    color: var(--white);
    font-family: "Carlito", Calibri, sans-serif;
    font-size: 11.2px;
    line-height: 17.3px;
    text-align: justify;
  }
  .intro p { margin: 0 0 9px 0; }

  .feature-photo {
    position: absolute;
    left: 26px;
    top: 460px;
    width: 523px;
    height: 345px;
    border-radius: 0 28px 0 0;
    background: linear-gradient(160deg, #f4f4f2 0%, #dcdcd8 45%, #b9bab6 100%);
  }

  .folio {
    position: absolute;
    bottom: 0;
    width: 13px;
    height: 42px;
    background: var(--folio);
    color: var(--white);
    font-family: "Carlito", Calibri, sans-serif;
    font-weight: 700;
    font-size: 9px;
    text-align: center;
    padding-top: 2px;
    box-sizing: border-box;
  }
  .page--left .folio { left: 26px; }
  .page--right .folio { left: 517px; }

  .comparison {
    position: absolute;
    left: 21px;
    top: 82px;
    width: 522px;
    height: 695px;
    background: var(--white);
  }
  .comparison table {
    width: 100%;
    border-collapse: collapse;
    table-layout: fixed;
    font-family: "PT Sans", "Myriad Pro", sans-serif;
    font-size: 10.4px;
    line-height: 14.2px;
    color: var(--ink);
  }
  .comparison td, .comparison th {
    vertical-align: top;
    text-align: left;
    font-weight: 400;
    padding: 2px 4px 0 4px;
    border-bottom: 1px solid var(--rule);
    border-left: 1px solid var(--rule);
  }
  .comparison tr > :first-child { border-left: none; }
  .comparison .row-head th { height: 22px; }
  .row-cost td { height: 96px; }
  .row-roi td { height: 108px; }
  .row-access td { height: 78px; }
  .row-time td { height: 176px; }
  .row-target td { height: 92px; }
  .row-change td { height: 107px; border-bottom: none; }
</style>
</head>
<body>
<main class="canvas">

  <section class="page page--left">
    <div class="section-tab">SEO</div>
    <aside class="fact fact--left">
      <span class="fact__label"><svg viewBox="0 0 10 10" aria-hidden="true"><path d="M5 9 L1 5 A2.2 2.2 0 0 1 5 2 A2.2 2.2 0 0 1 9 5 Z" fill="var(--dark-orange)"/></svg>Did you know that...?</span>
      More than 87800000000000 (87.8 billion) searches are conducted<br>on Searchly every month that’s a lot of potential customers
    </aside>

    <div class="intro">
      <p>Velmora Outcomes doesn’t believe that traditional marketing is finished and out of the fight, but it does believe that Traditional Marketing without SEO is. However, imagine hiring a sales man who works 24 hours a day, 7 days a week, who can deal with hundreds and thousands of customers at the same time and still personalize the response to consumer. Sounds amazing, right? That’s not all - he wants to work for very little money. Who is this sales man?</p>
      <p>The Sales man is actually all of the international search engines. Search engines deal with over 120 billion plus searches every month.</p>
      <p>How do I Turn a Search engine into my personal sales man?</p>
      <p>People trust search engines so if the search engine suggests say this sit is the best people trust it and visit the site. So how do I get a search engine to suggest my site?</p>
      <p>To understand SEO you have to understand search engines. Search engines visit more than 40 billion pages a day and add them to their databases of pages. During this process it gives each page a page rank. This rank is based on a very complex equation containing many factors. They also create lists of ‘keywords’ that it associates to the website and it gathers other information ie link to other sites, amount of time a user spends on a page and much more.When a user searches for a word, search engines use all of this data to calculate the order it displays the results. However this is not the end of it search engines also change the results based on how popular a page or site is, so the more popular you are the more the visits you get.</p>
      <p>&nbsp;SEO is about understanding this process and ensuring that you site is popular and ticks the right boxes. So let the experts at Velmora Outcomes get your website to the front page - all you have to do is sit back and enjoy the rewards.</p>
    </div>

    <div class="feature-photo" role="img" aria-label="Photo of a spiral notepad with a hand-drawn SEO mind map (keyword research, title tags, page content, social media, traffic monitoring), glasses and a pen"></div>
    <div class="folio">2</div>
  </section>

  <section class="page page--right">
    <aside class="fact fact--right">
      <span class="fact__label">Did you know that...?<svg viewBox="0 0 10 10" aria-hidden="true"><path d="M5 9 L1 5 A2.2 2.2 0 0 1 5 2 A2.2 2.2 0 0 1 9 5 Z" fill="var(--dark-orange)"/></svg></span>
      Searchly owns 65-70% of the international<br>search engine market share.
    </aside>
    <div class="section-tab">SEO</div>

    <div class="comparison">
      <table>
        <colgroup>
          <col style="width:102px"><col style="width:63px"><col style="width:140px"><col style="width:91px"><col style="width:126px">
        </colgroup>
        <tr class="row-head"><th></th><th colspan="2">Online Marketing and SEO</th><th colspan="2">Traditional???</th></tr>
        <tr class="row-cost"><td>Cost</td><td>Low Cost</td><td>SEO cost are lower than traditional marketing cost and reach an international audience</td><td>High Cost</td><td>Human Resources cost a lot of money.<br><br style="line-height:6px">Media coverage costs a lot of money</td></tr>
        <tr class="row-roi"><td>Return On Investment</td><td>Low Risk/High Return</td><td>Due to its low implementation costs, SEO has a very high return on investment (ROI). This reduces the risk you need to take to maintain or increase profits</td><td>High Risk /Low To Medium Return</td><td>Traditional marketing involves high up-front costs that may never return your original investment.</td></tr>
        <tr class="row-access"><td>Availability to Business</td><td>Any size business</td><td>Due to low cost and high return SEO is available to any business</td><td>Medium to large corporations</td><td>Due to media costs it is virtual impossible to get wide national coverage for a small company</td></tr>
        <tr class="row-time"><td>Time required</td><td>Low</td><td>Imagine your business running 24 hours day. With SEO, potential customers can visit you website from anywhere at any time. They can even purchase goods whilst you’re asleep. With online marketing we can personalize automated emails to entice more purchases</td><td>High</td><td>Direct marketing requires a physical person to be interacting with the customer and even the best sales man can’t do this 24 hours a day</td></tr>
        <tr class="row-target"><td>Ability to target audience</td><td>Easy</td><td>By its very nature, SEO only targets those that are interested in your field or product - the bonus is that your audience is from all over the world</td><td>Difficult and costly</td><td>Traditional media is limited to either a small target audience or a wide non-targeted audience. Internet marketing allows both.</td></tr>
        <tr class="row-change"><td>Change marketing based on feedback</td><td>Very Simple</td><td>Internet marketing is all about helping you tailoring and automating what the consumer sees, based on feedback, &nbsp;to increase your return on investment</td><td></td><td>Traditional marketing takes time to update and distribute, even in the best case scenario you have to update your brochure and get it printed.</td></tr>
      </table>
    </div>
    <div class="folio">5</div>
  </section>

</main>
</body>
</html>
```